PowerPoint design of key models

We recently had a new PPT template created which we are very happy with. Now we want to have some of our key models on various pages in PPT to be reformatted and redesigned to match the other graphics of the new PT template. Can you please redesign the models and graphics so they have the same look and feel as the new template. I have included both files for you to work with. Thank you.

```html
<!DOCTYPE html>
<html lang="en">
<head>
<meta charset="utf-8">
<title>Key Models – Slide Set</title>
<link href="https://fonts.googleapis.com/css2?family=Ubuntu:ital,wght@0,400;0,500;0,700;1,400&display=swap" rel="stylesheet">
<style>
  :root{
    --navy:#1e2459;
    --ink:#14213d;
    --black:#111111;
    --blue:#1b6ab5;
    --sky:#23aee5;
    --cyan:#29abe2;
    --pale:#8fb4df;
    --text:#1c1c24;
    --grey:#555a66;
    --photo:#2b5592;
    --deep:#1a2550;
  }
  html,body{margin:0;padding:0;width:1200px;height:847px;overflow:hidden;background:#fff}
  .deck{display:block;width:1200px;height:847px;font-family:"Ubuntu",sans-serif}
  .divider{stroke:var(--cyan);stroke-width:3}
  .brand-dot{fill:var(--blue)}
  .brand-name{font-size:13px;font-weight:700;fill:var(--navy)}
  .title-bar{fill:var(--blue)}
  .title{font-size:27px;fill:var(--text)}
  .title-navy{font-size:27px;fill:var(--navy)}
  .url{font-size:8px;fill:var(--text)}
  .band{fill:url(#bandGrad)}
  .copy{font-size:6px;fill:#fff;text-anchor:middle}
  .page-box{fill:var(--ink)}
  .page-num{font-size:9px;font-weight:700;fill:#fff;text-anchor:middle}
  .body{font-size:13px;fill:var(--text)}
  .small{font-size:10px;fill:var(--text)}
  .tiny-bullet{fill:none;stroke:var(--cyan);stroke-width:1}
  .label-white{fill:#fff;font-weight:700;text-anchor:middle}
  .mid{text-anchor:middle}
  .accent{fill:var(--cyan)}
  .knob-edge{fill:none;stroke:#fff;stroke-width:4}
  .icon-line{fill:none;stroke:#fff;stroke-width:2;stroke-linecap:round;stroke-linejoin:round}
</style>
</head>
<body>
<svg class="deck" viewBox="0 0 2295 1621" width="1200" height="847" xmlns="http://www.w3.org/2000/svg">
  <defs>
    <linearGradient id="bandGrad" x1="0" x2="1" y1="0" y2="0">
      <stop offset="0" stop-color="#29abe2"/><stop offset="1" stop-color="#1b6ab5"/>
    </linearGradient>
    <linearGradient id="discGrad" x1="0" x2="1" y1="0" y2="1">
      <stop offset="0" stop-color="#29abe2"/><stop offset="1" stop-color="#1b6ab5"/>
    </linearGradient>
  </defs>

  <!-- grid dividers -->
  <line class="divider" x1="749" y1="0" x2="749" y2="1621"/>
  <line class="divider" x1="1527" y1="0" x2="1527" y2="1621"/>
  <line class="divider" x1="0" y1="547" x2="2295" y2="547"/>
  <line class="divider" x1="0" y1="1101" x2="2295" y2="1101"/>

  <!-- Slide 2: modern consultant -->
  <g class="slide slide-consultant">
    <circle class="brand-dot" cx="609" cy="58" r="9"/><text class="brand-name" x="622" y="63">Apex Talent</text>
    <rect class="title-bar" x="73" y="95" width="30" height="6"/>
    <text x="113" y="104" font-size="28" font-weight="700" fill="#111">The modern recruitment consultant</text>
    <text x="64" y="140" font-size="19" font-weight="700" class="accent">Success in recruitment today is evolving and changing</text>
    <g font-size="19" fill="#1c1c24">
      <circle class="tiny-bullet" cx="78" cy="160" r="4"/><text x="97" y="166">It has never been about being pushy – that hasn’t changed</text>
      <circle class="tiny-bullet" cx="78" cy="186" r="4"/><text x="97" y="192">And relying on old fashioned relationships alone is not enough</text>
      <circle class="tiny-bullet" cx="78" cy="212" r="4"/><text x="97" y="218">Today it is about <tspan class="accent" font-weight="700">advice, problem solving and value creation</tspan></text>
      <text x="97" y="245">– not just the services</text>
    </g>
    <g font-size="14" font-style="italic" class="mid" fill="#29abe2">
      <text x="245" y="302">“My job is to be a resource</text>
      <text x="245" y="322">for my educators and clients,</text>
      <text x="245" y="342">to stand out because I</text>
      <text x="245" y="362"><tspan fill="#1b6ab5" font-weight="700">help them to be successful</tspan>.</text>
      <text x="245" y="402">I realise that developing business is</text>
      <text x="245" y="421" fill="#555a66">how I contribute to the <tspan text-decoration="underline">a</tspan> team!”</text>
    </g>
    <rect x="452" y="260" width="251" height="215" fill="var(--photo)" role="img" aria-label="Photo of a consultant meeting with a client"/>
    <text class="url" x="38" y="510">www.apextalent.com</text>
    <polygon class="band" points="142,498 662,498 657,515 137,515"/>
    <text class="copy" x="400" y="509">Copyright @Apex Talent 2024</text>
    <polygon class="page-box" points="673,498 709,498 704,515 668,515"/><text class="page-num" x="688" y="510">2</text>
  </g>

  <!-- Slide 6: value chain -->
  <g class="slide slide-value-chain">
    <circle class="brand-dot" cx="1381" cy="57" r="9"/><text class="brand-name" x="1394" y="62">Apex Talent</text>
    <rect class="title-bar" x="809" y="78" width="32" height="6"/>
    <text class="title-navy" x="849" y="90">Positioning on The Value Chain</text>
    <text x="810" y="115" font-size="13" font-weight="700" class="accent">Questions:</text>
    <text class="body" x="810" y="145">Where are you today?</text>
    <text class="body" x="810" y="176">What does it take to move up?</text>
    <text class="body" x="810" y="207">What is your customer looking for?</text>
    <circle cx="1138" cy="242" r="49" fill="var(--blue)"/>
    <circle cx="1231" cy="335" r="49" fill="var(--sky)"/>
    <circle cx="1048" cy="335" r="49" fill="#1a2a55"/>
    <circle cx="1138" cy="415" r="49" fill="var(--ink)"/>
    <g font-size="15" font-weight="700">
      <text x="1200" y="244" fill="#1b6ab5">1. Order Taker</text>
      <text x="1295" y="341" fill="#23aee5">2. Transactional Trader</text>
      <text x="987" y="341" fill="#1e2459" text-anchor="end">3. Solutions Provider</text>
      <text x="1076" y="429" fill="#1e2459" text-anchor="end">4. Trusted Advisor</text>
    </g>
    <text class="url" x="794" y="521">www.apextalent.com</text>
    <polygon class="band" points="902,510 1436,510 1431,527 897,527"/>
    <text class="copy" x="1166" y="521">Copyright @Apex Talent 2024</text>
    <polygon class="page-box" points="1447,510 1484,510 1479,527 1442,527"/><text class="page-num" x="1462" y="522">6</text>
  </g>

  <!-- Slide 7: three demands -->
  <g class="slide slide-stretch">
    <circle class="brand-dot" cx="2153" cy="65" r="9"/><text class="brand-name" x="2166" y="70">Apex Talent</text>
    <rect class="title-bar" x="1617" y="96" width="32" height="6"/>
    <text x="1666" y="105" font-size="27" font-weight="500" fill="var(--navy)">The Stretch: Balancing Three Competing</text>
    <text x="1666" y="140" font-size="27" font-weight="500" fill="var(--navy)">Demands</text>
    <g stroke-linejoin="round" stroke-width="14">
      <polygon points="1925,142 2000,268 1925,312 1850,268" fill="var(--ink)" stroke="var(--ink)"/>
      <polygon points="1834,292 1913,336 1913,421 1766,421" fill="var(--blue)" stroke="var(--blue)"/>
      <polygon points="2013,292 1937,336 1937,421 2085,421" fill="var(--sky)" stroke="var(--sky)"/>
    </g>
    <text class="label-white" x="1925" y="252" font-size="12">TASK</text>
    <text class="label-white" x="1849" y="370" font-size="12">TEAM</text>
    <text class="label-white" x="1992" y="370" font-size="12">INDIVIDUAL</text>
    <text class="url" x="1590" y="510">www.apextalent.com</text>
    <polygon class="band" points="1693,498 2206,498 2201,515 1688,515"/>
    <text class="copy" x="1947" y="509">Copyright @Apex Talent 2024</text>
    <polygon class="page-box" points="2217,498 2252,498 2247,515 2212,515"/><text class="page-num" x="2231" y="510">7</text>
  </g>

  <!-- Slide 8: coaching traits -->
  <g class="slide slide-traits">
    <circle class="brand-dot" cx="625" cy="590" r="9"/><text class="brand-name" x="638" y="595">Apex Talent</text>
    <rect class="title-bar" x="61" y="635" width="34" height="6"/>
    <text class="title-navy" x="96" y="646">The 4 Essential Coaching Traits</text>
    <g class="puzzle-wheel">
      <g stroke="#fff" stroke-width="4">
        <path d="M208,843 A126,126 0 0 1 334,717 L334,780 A63,63 0 0 0 271,843 Z" fill="var(--black)"/>
        <path d="M334,717 A126,126 0 0 1 460,843 L397,843 A63,63 0 0 0 334,780 Z" fill="var(--sky)"/>
        <path d="M460,843 A126,126 0 0 1 334,969 L334,906 A63,63 0 0 0 397,843 Z" fill="var(--deep)"/>
        <path d="M334,969 A126,126 0 0 1 208,843 L271,843 A63,63 0 0 0 334,906 Z" fill="var(--blue)"/>
      </g>
      <!-- interlocking tabs -->
      <circle cx="343" cy="750" r="11" fill="var(--black)"/>
      <rect x="330" y="744" width="6" height="12" fill="var(--black)"/>
      <path class="knob-edge" d="M334,743.7 A11,11 0 1 1 334,756.3"/>
      <circle cx="428" cy="852" r="11" fill="var(--sky)"/>
      <rect x="422" y="840" width="12" height="6" fill="var(--sky)"/>
      <path class="knob-edge" d="M421.7,843 A11,11 0 1 0 434.3,843"/>
      <circle cx="325" cy="937" r="11" fill="var(--deep)"/>
      <rect x="332" y="931" width="6" height="12" fill="var(--deep)"/>
      <path class="knob-edge" d="M334,930.7 A11,11 0 1 0 334,943.3"/>
      <circle cx="240" cy="834" r="11" fill="var(--blue)"/>
      <rect x="234" y="840" width="12" height="6" fill="var(--blue)"/>
      <path class="knob-edge" d="M233.7,843 A11,11 0 1 1 246.3,843"/>
    </g>
    <g class="icon-line" stroke-width="2.5">
      <rect x="251" y="765" width="30" height="22" rx="2"/>
      <circle cx="260" cy="774" r="3"/><path d="M255,783 q5,-6 10,0 M269,772 h8 M269,778 h8"/>
      <path d="M410,770 h14 v11 h-8 l-4,4 v-4 h-2 z"/>
      <circle cx="404" cy="790" r="4"/><path d="M396,804 q8,-12 16,0"/>
      <path d="M254,903 v-6 q-4,-2 -2,-8 q2,-10 12,-10 q10,0 10,10 q0,6 -4,8 v6"/>
      <circle cx="262" cy="890" r="4"/>
      <circle cx="398" cy="910" r="11"/><circle cx="398" cy="910" r="5"/>
      <path d="M398,910 l14,-12"/>
    </g>
    <circle class="brand-dot" cx="297" cy="843" r="8"/>
    <text x="307" y="847" font-size="11" font-weight="700" fill="var(--navy)">Apex Talent</text>
    <g font-size="13" font-weight="700" fill="var(--navy)">
      <text x="94" y="747">PRESENCE</text>
      <text x="469" y="745">QUESTIONING</text>
      <text x="97" y="911">BEHAVIOROR FLEX</text>
      <text x="469" y="903">MEASUREMENT &amp; FEEDBACK</text>
    </g>
    <g class="small">
      <circle class="tiny-bullet" cx="103" cy="763" r="2.5"/><text x="113" y="766">Logged on</text>
      <circle class="tiny-bullet" cx="103" cy="775" r="2.5"/><text x="113" y="778">Mindful state</text>
      <circle class="tiny-bullet" cx="103" cy="787" r="2.5"/><text x="113" y="790">Manage climate</text>
      <circle class="tiny-bullet" cx="103" cy="799" r="2.5"/><text x="113" y="802">Observations</text>
      <circle class="tiny-bullet" cx="472" cy="759" r="2.5"/><text x="481" y="762">Ask, don’t Tell</text>
      <circle class="tiny-bullet" cx="472" cy="771" r="2.5"/><text x="481" y="774">Use a Variety of Questions</text>
      <circle class="tiny-bullet" cx="87" cy="921" r="2.5"/><text x="96" y="924">From High control</text>
      <circle class="tiny-bullet" cx="87" cy="933" r="2.5"/><text x="96" y="936">To Low control</text>
      <circle class="tiny-bullet" cx="472" cy="917" r="2.5"/><text x="481" y="920">5 levels of Listening</text>
      <circle class="tiny-bullet" cx="472" cy="929" r="2.5"/><text x="481" y="932">Be an Active Listener</text>
    </g>
    <text class="url" x="30" y="1059">www.apextalent.com</text>
    <polygon class="band" points="139,1047 681,1047 676,1065 134,1065"/>
    <text class="copy" x="390" y="1058">Copyright @Apex Talent 2024</text>
    <polygon class="page-box" points="691,1047 729,1047 724,1065 686,1065"/><text class="page-num" x="707" y="1059">8</text>
  </g>

  <!-- Slide 9: timeline -->
  <g class="slide slide-timeline">
    <circle class="brand-dot" cx="1387" cy="591" r="9"/><text class="brand-name" x="1400" y="596">Apex Talent</text>
    <rect class="title-bar" x="841" y="645" width="34" height="6"/>
    <text x="883" y="660" font-size="33" font-weight="700" fill="var(--navy)">Company Timeline</text>
    <text x="848" y="774" font-size="15" font-style="italic" class="accent">This is how we structure our calls</text>
    <polygon points="846,798 958,798 998,838 958,879 846,879 886,838" fill="var(--blue)"/>
    <polygon points="976,798 1088,798 1128,838 1088,879 976,879 1016,838" fill="var(--ink)"/>
    <polygon points="1106,798 1218,798 1258,838 1218,879 1106,879 1146,838" fill="var(--blue)"/>
    <polygon points="1238,798 1350,798 1390,838 1350,879 1238,879 1278,838" fill="var(--ink)"/>
    <g font-size="17">
      <text class="label-white" x="921" y="844">PLAN</text>
      <text class="label-white" x="1065" y="844">RECRUITE</text>
      <text class="label-white" x="1191" y="844">EXECUTE</text>
      <text class="label-white" x="1320" y="844">SUSTAIN</text>
    </g>
    <text class="url" x="780" y="1070">www.apextalent.com</text>
    <polygon class="band" points="891,1057 1444,1057 1439,1076 886,1076"/>
    <text class="copy" x="1162" y="1069">Copyright @Apex Talent 2024</text>
    <polygon class="page-box" points="1455,1057 1492,1057 1487,1076 1450,1076"/><text class="page-num" x="1470" y="1070">9</text>
  </g>

  <!-- Slide 10: integrated learning -->
  <g class="slide slide-learning">
    <circle class="brand-dot" cx="2166" cy="593" r="9"/><text class="brand-name" x="2179" y="598">Apex Talent</text>
    <rect class="title-bar" x="1585" y="619" width="34" height="6"/>
    <text x="1634" y="630" font-size="31" font-weight="500" fill="#2b2f45">An integrated approach to learning</text>
    <g font-size="15" font-weight="700" fill="#111" class="mid">
      <text x="1796" y="675">Periodic Training</text>
      <text x="1680" y="972">Objective Feedback</text>
      <text x="1680" y="993">(via The Coaching Action Tool)</text>
      <text x="1951" y="972">Regular Coaching</text>
    </g>
    <polygon points="1800,697 1928,951 1672,951" fill="var(--navy)"/>
    <polygon points="1736,823 1864,823 1800,951" fill="var(--sky)" stroke="#fff" stroke-width="2"/>
    <g font-size="9" class="label-white">
      <text x="1800" y="841">Developing</text><text x="1800" y="853">High</text>
      <text x="1800" y="865">Performance</text><text x="1800" y="877">Consultants</text>
    </g>
    <g font-size="13" fill="#1c1c24">
      <rect x="1981" y="710" width="4" height="4" fill="var(--cyan)"/>
      <text x="2008" y="719">Instalments of <tspan font-weight="700">training</tspan> over time:</text>
      <text x="2008" y="738">Externally delivered workshops</text>
      <text x="2008" y="757">and Internally delivered reinforcement</text>
      <rect x="1981" y="786" width="4" height="4" fill="var(--cyan)"/>
      <text x="2008" y="795">Regular <tspan font-weight="700">coaching</tspan> sessions with</text>
      <text x="2008" y="814">your manager</text>
      <rect x="1981" y="842" width="4" height="4" fill="var(--cyan)"/>
      <text x="2008" y="851">Objective <tspan font-weight="700">feedback</tspan> on strengths</text>
      <text x="2008" y="870">and development opportunities</text>
      <text x="2008" y="889">using the <tspan font-weight="700">Coaching Action Tool</tspan></text>
    </g>
    <text class="url" x="1559" y="1071">www.apextalent.com</text>
    <polygon class="band" points="1669,1059 2222,1059 2217,1078 1664,1078"/>
    <text class="copy" x="1940" y="1071">Copyright @Apex Talent 2024</text>
    <polygon class="page-box" points="2233,1059 2270,1059 2265,1078 2228,1078"/><text class="page-num" x="2248" y="1072">10</text>
  </g>

  <!-- Slide 11: development system -->
  <g class="slide slide-system">
    <circle class="brand-dot" cx="623" cy="1138" r="9"/><text class="brand-name" x="636" y="1143">Apex Talent</text>
    <rect class="title-bar" x="56" y="1155" width="32" height="6"/>
    <text class="title" x="95" y="1165">The Norvale development system</text>
    <g stroke="var(--cyan)" stroke-width="2">
      <line x1="339" y1="1263" x2="434" y2="1263"/>
      <line x1="339" y1="1420" x2="434" y2="1420"/>
      <line x1="256" y1="1318" x2="256" y2="1368"/>
      <line x1="518" y1="1318" x2="518" y2="1368"/>
    </g>
    <g fill="var(--navy)">
      <rect x="174" y="1211" width="165" height="107"/>
      <rect x="434" y="1211" width="165" height="107"/>
      <rect x="174" y="1368" width="165" height="107"/>
      <rect x="434" y="1368" width="165" height="107"/>
    </g>
    <g font-size="15" class="label-white">
      <text x="256" y="1250">PRES</text><text x="256" y="1270">Call Sequence</text>
      <text x="517" y="1260">10 Step Coaching</text><text x="517" y="1281">Process</text>
      <text x="256" y="1418">RECRUIT</text><text x="256" y="1438">BD Process</text>
      <text x="517" y="1428">Coaching Action Tool</text>
    </g>
    <text x="372" y="1527" font-size="17" fill="#333" class="mid">Supporting your growth as a</text>
    <text x="372" y="1550" font-size="17" fill="#333" class="mid">high performance consultant</text>
    <text class="url" x="34" y="1603">www.apextalent.com</text>
    <polygon class="band" points="142,1590 679,1590 674,1609 137,1609"/>
    <text class="copy" x="390" y="1602">Copyright @Apex Talent 2024</text>
    <polygon class="page-box" points="689,1590 725,1590 720,1609 684,1609"/><text class="page-num" x="703" y="1603">11</text>
  </g>

  <!-- Slide 12: plan the how -->
  <g class="slide slide-how">
    <circle class="brand-dot" cx="1395" cy="1131" r="9"/><text class="brand-name" x="1408" y="1136">Apex Talent</text>
    <rect class="title-bar" x="819" y="1153" width="32" height="6"/>
    <text class="title" x="860" y="1164">Now plan the HOW</text>
    <text x="817" y="1213" font-size="23" font-weight="700" class="accent">How will you achieve your pre planned BD goal?</text>
    <path d="M872,1245 Q1000,1400 872,1560" fill="none" stroke="var(--cyan)" stroke-width="1.5"/>
    <rect x="910" y="1270" width="448" height="66" fill="var(--navy)"/>
    <rect x="935" y="1370" width="423" height="65" fill="var(--blue)"/>
    <rect x="910" y="1469" width="448" height="66" fill="var(--navy)"/>
    <circle cx="910" cy="1303" r="40" fill="url(#discGrad)" stroke="#fff" stroke-width="3"/>
    <circle cx="935" cy="1402" r="40" fill="url(#discGrad)" stroke="#fff" stroke-width="3"/>
    <circle cx="910" cy="1502" r="40" fill="url(#discGrad)" stroke="#fff" stroke-width="3"/>
    <g fill="none" stroke="#fff" stroke-width="3" stroke-linecap="round" stroke-linejoin="round">
      <path d="M895,1290 h30 v18 h-16 l-8,7 v-7 h-6 z"/>
      <path d="M918,1396 h34 m-8,-7 l8,7 l-8,7 M952,1410 h-34 m8,-7 l-8,7 l8,7"/>
      <path d="M898,1492 L922,1490 L912,1514 Z"/>
    </g>
    <g fill="#fff"><circle cx="898" cy="1492" r="5"/><circle cx="922" cy="1490" r="5"/><circle cx="912" cy="1514" r="5"/></g>
    <g font-size="24" font-weight="700" fill="#fff">
      <text x="964" y="1312">Questions to ask?</text>
      <text x="988" y="1411">Solutions to needs?</text>
      <text x="964" y="1511">Objections to overcome?</text>
    </g>
    <text class="url" x="800" y="1601">www.apextalent.com</text>
    <polygon class="band" points="910,1589 1451,1589 1446,1607 905,1607"/>
    <text class="copy" x="1178" y="1600">Copyright @Apex Talent 2024</text>
    <polygon class="page-box" points="1462,1589 1497,1589 1492,1607 1457,1607"/><text class="page-num" x="1476" y="1601">12</text>
  </g>

  <!-- Slide 13: relationship -->
  <g class="slide slide-relationship">
    <circle class="brand-dot" cx="2157" cy="1134" r="9"/><text class="brand-name" x="2170" y="1139">Apex Talent</text>
    <rect class="title-bar" x="1583" y="1153" width="32" height="6"/>
    <text class="title" x="1621" y="1164">Build a relationship  – 5 considerations</text>
    <line x1="1645" y1="1405" x2="1535" y2="1462" stroke="var(--navy)" stroke-width="22" stroke-linecap="round"/>
    <circle cx="1727" cy="1355" r="100" fill="#fff" stroke="var(--navy)" stroke-width="9"/>
    <g stroke="#fff" stroke-width="2">
      <path d="M1727,1355 L1727,1269 A86,86 0 0 1 1808.8,1328.4 Z" fill="var(--navy)"/>
      <path d="M1727,1355 L1808.8,1328.4 A86,86 0 0 1 1777.6,1424.6 Z" fill="var(--blue)"/>
      <path d="M1727,1355 L1777.6,1424.6 A86,86 0 0 1 1676.4,1424.6 Z" fill="var(--sky)"/>
      <path d="M1727,1355 L1676.4,1424.6 A86,86 0 0 1 1645.2,1328.4 Z" fill="var(--pale)"/>
      <path d="M1727,1355 L1645.2,1328.4 A86,86 0 0 1 1727,1269 Z" fill="var(--black)"/>
    </g>
    <g class="icon-line">
      <!-- balance scale -->
      <path d="M1700,1293 v30 M1690,1323 h20 M1685,1300 h30 M1685,1300 l-6,12 h12 z M1715,1300 l-6,12 h12 z"/>
      <!-- stacked documents -->
      <rect x="1744" y="1294" width="18" height="22"/>
      <path d="M1748,1294 v-4 h18 v22 h-4 M1748,1300 h10 M1748,1305 h10 M1748,1310 h10"/>
      <!-- gavel -->
      <path d="M1766,1364 l10,-10 l8,8 l-10,10 z M1771,1367 l-11,11 M1756,1388 h20"/>
      <!-- chevrons -->
      <path d="M1712,1403 l8,8 l-8,8 M1724,1403 l8,8 l-8,8 M1736,1403 l8,8 l-8,8"/>
      <!-- certificate -->
      <rect x="1663" y="1350" width="22" height="28"/>
      <path d="M1667,1356 h14 M1667,1361 h14 M1667,1366 h8"/>
      <circle cx="1680" cy="1372" r="3"/>
    </g>
    <g fill="var(--navy)">
      <circle cx="1876" cy="1231" r="21"/><circle cx="1876" cy="1311" r="21"/>
      <circle cx="1876" cy="1383" r="21"/><circle cx="1876" cy="1455" r="21"/><circle cx="1876" cy="1532" r="21"/>
    </g>
    <g font-size="15" class="label-white" font-weight="400">
      <text x="1876" y="1236">01</text><text x="1876" y="1316">02</text><text x="1876" y="1388">03</text>
      <text x="1876" y="1460">04</text><text x="1876" y="1537">05</text>
    </g>
    <g font-size="14" font-weight="700" fill="var(--navy)">
      <text x="1916" y="1218">Detection</text><text x="1914" y="1289">Connection</text>
      <text x="1916" y="1367">Alignment</text><text x="1916" y="1441">Collaboration</text>
      <text x="1916" y="1518">Authenticity</text>
    </g>
    <g font-size="12" fill="#1c1c24">
      <circle class="tiny-bullet" cx="1921" cy="1233" r="2.5"/><text x="1933" y="1237">Get your radar on to read the climate</text>
      <circle class="tiny-bullet" cx="1921" cy="1249" r="2.5"/><text x="1933" y="1253">What can you observe, hear, sense</text>
      <circle class="tiny-bullet" cx="1921" cy="1305" r="2.5"/><text x="1933" y="1309">Use empathy to build a bridge</text>
      <circle class="tiny-bullet" cx="1921" cy="1321" r="2.5"/><text x="1933" y="1325">Get them talking about themselves</text>
      <circle class="tiny-bullet" cx="1921" cy="1382" r="2.5"/><text x="1933" y="1386">Find what you have in common</text>
      <circle class="tiny-bullet" cx="1921" cy="1398" r="2.5"/><text x="1933" y="1402">Maximise similarities and minimise differences</text>
      <circle class="tiny-bullet" cx="1921" cy="1455" r="2.5"/><text x="1933" y="1459">Create a shared experience - get them involved early</text>
      <circle class="tiny-bullet" cx="1921" cy="1471" r="2.5"/><text x="1933" y="1475">Work on an activity together – probing, solving, options,</text>
      <circle class="tiny-bullet" cx="1921" cy="1487" r="2.5"/><text x="1933" y="1491">inspecting</text>
      <circle class="tiny-bullet" cx="1921" cy="1531" r="2.5"/><text x="1933" y="1535">Be genuine and keep it real</text>
      <circle class="tiny-bullet" cx="1921" cy="1547" r="2.5"/><text x="1933" y="1551">Don’t overdo your energy or confidence – be your best</text>
      <text x="1933" y="1567">you!</text>
    </g>
    <text class="url" x="1560" y="1606">www.apextalent.com</text>
    <polygon class="band" points="1668,1593 2212,1593 2207,1612 1663,1612"/>
    <text class="copy" x="1937" y="1605">Copyright @Apex Talent 2024</text>
    <polygon class="page-box" points="2223,1593 2258,1593 2253,1612 2218,1612"/><text class="page-num" x="2238" y="1606">13</text>
  </g>
</svg>
</body>
</html>
```